BRIGHT COLORFUL + 55 FAMILY HISTORY BROCHURE 11 x 17 bifold

11 x 17 Bifold Flyer I have given you the Layout I just need you to make it Pretty

YOU DO NOT NEED TO FOLLOW MY LAYOUT, You can but dont have too

Target Market(s)

55 year old consumers, who could choose our service of Hereditary Cancer Screening

Industry/Entity Type

Health And Wellness

Requirements
Must have
• Must be appealing to Grand Parents, must make them want to test , show lots of pictures of grand children, YOU DO NOT NEED TO FOLLOW MY LAYOUT , You can but dont have too
Nice to have
• use our colors of our logo , YOU DO NOT NEED TO FOLLOW MY LAYOUT , You can but dont have too
Should not have
• YOU DO NOT NEED TO FOLLOW MY LAYOUT, You can but dont have too

```html
<!DOCTYPE html>
<html lang="en">
<head>
<meta charset="utf-8">
<title>Hereditary Cancer Screening Bifold</title>
<link href="https://fonts.googleapis.com/css2?family=Open+Sans:wght@400;600;700;800&family=Noto+Serif:wght@400&family=Roboto+Condensed:wght@400&display=swap" rel="stylesheet">
<style>
  :root {
    --navy: #1c2a5c;
    --green: #3cb54a;
    --lime: #8dc63f;
    --panel-grey: #ececec;
    --page-bg: #e4e4e4;
    --overlay: rgba(52, 58, 96, 0.72);
    --white: #ffffff;
  }
  * { box-sizing: border-box; margin: 0; padding: 0; }
  html, body { width: 1200px; height: 1200px; overflow: hidden; }
  body {
    background: var(--page-bg);
    font-family: "Open Sans", sans-serif;
    color: var(--navy);
    position: relative;
  }
  .spread {
    position: absolute;
    left: 40px; top: 170px;
    width: 1120px; height: 860px;
    display: flex;
  }
  .panel {
    position: relative;
    width: 560px; height: 860px;
    overflow: hidden;
  }
  .panel--inside { background: var(--panel-grey); }
  .panel--cover { background: var(--white); }
  .panel-art { position: absolute; left: 0; top: 0; width: 560px; height: 480px; }

  .overlay-box {
    position: absolute;
    left: 38px; width: 492px;
    background: var(--overlay);
    color: var(--white);
    font-family: "Noto Serif", serif;
    text-align: center;
    padding: 6px 10px;
  }
  .overlay-box--decision { top: 148px; height: 88px; font-size: 17px; line-height: 27px; color: #e6e8f0; }
  .overlay-box--question { top: 247px; height: 74px; font-size: 18px; line-height: 30px; padding-top: 6px; }

  .inside-copy {
    position: absolute;
    left: 12px; right: 10px; top: 470px;
    font-size: 18.5px; line-height: 25px;
    color: #1a1f3a;
  }
  .inside-copy .lead { font-size: 24.5px; font-weight: 700; line-height: 31px; color: var(--navy); }
  .inside-copy .emphasis { font-weight: 700; color: var(--navy); }

  .web-box {
    position: absolute;
    background: var(--green);
    color: var(--white);
    text-align: center;
  }
  .web-box--large {
    left: 101px; top: 736px; width: 360px; height: 56px;
    font-family: "Roboto Condensed", sans-serif;
    font-size: 33px; line-height: 56px;
  }
  .web-box--small {
    left: 178px; top: 779px; width: 214px; height: 21px;
    font-size: 13px; line-height: 21px; font-style: italic;
  }

  .brand-block {
    position: absolute;
    left: 285px; top: 30px; width: 275px; height: 110px;
    background: rgba(255,255,255,0.93);
    display: flex; align-items: center; gap: 12px;
    padding-left: 18px;
  }
  .brand-dot { width: 58px; height: 58px; border-radius: 50%; background: var(--green); flex: none; }
  .brand-name {
    font-weight: 800; font-size: 24px; line-height: 27px;
    color: var(--navy); letter-spacing: 1px; text-transform: uppercase;
  }

  .cover-title {
    position: absolute; left: 0; right: 0; top: 478px;
    text-align: center; font-weight: 800; font-size: 33px; color: var(--navy);
  }
  .cover-subtitle {
    position: absolute; left: 0; right: 0; top: 526px;
    text-align: center; font-weight: 600; font-size: 28px; color: var(--green);
  }
  .photo-strip {
    position: absolute; left: 0; top: 569px; width: 560px; height: 137px;
    display: flex;
  }
  .photo-strip .photo { height: 100%; }
  .photo--a { width: 142px; background: linear-gradient(160deg, #8fae6a, #d9b9a0 60%, #6d5a48); }
  .photo--b { width: 145px; background: linear-gradient(170deg, #d9dcd6, #b45a4c 55%, #5a3a2e); }
  .photo--c { width: 142px; background: linear-gradient(165deg, #a9c48a, #e7c6ad 50%, #c86a7e); }
  .photo--d { width: 131px; background: linear-gradient(175deg, #c4cfc4, #e8c2a6 55%, #c9b9a3); }
  .caption-bar {
    position: absolute; left: 0; top: 706px; width: 560px; height: 24px;
    background: var(--green); color: var(--white);
    font-weight: 700; font-size: 13px; line-height: 24px; text-align: center;
  }
  .cover-tagline {
    position: absolute; left: 0; right: 0; top: 746px;
    text-align: center; font-weight: 600; font-size: 18.5px; color: var(--navy);
  }
</style>
</head>
<body>
<div class="spread">

  <section class="panel panel--inside">
    <svg class="panel-art" viewBox="0 0 560 480" role="img" aria-label="Photo of a smiling multigenerational family gathered in a kitchen">
      <defs>
        <linearGradient id="kitchenTone" x1="0" y1="0" x2="0" y2="1">
          <stop offset="0" stop-color="#6e6a70"/>
          <stop offset="0.5" stop-color="#8a7f80"/>
          <stop offset="1" stop-color="#b8aea6"/>
        </linearGradient>
      </defs>
      <path d="M0 30 H560 V452 Q280 440 0 400 Z" fill="url(#kitchenTone)"/>
      <path d="M0 400 Q280 440 560 452 V468 Q280 456 0 414 Z" fill="var(--green)"/>
    </svg>
    <div class="overlay-box overlay-box--decision">Your decision won’t just affect you. It will also impact Your Family, since your test results may Forecast Their Cancer Risks, too.</div>
    <div class="overlay-box overlay-box--question">DOES CANCER Run in Your Family ??<br>A Simple Swab Could SAVE a Family Members LIFE.</div>

    <p class="inside-copy">
      <span class="lead">We believe it is important to understand what can and cannot be learned with genetic testing.</span>
      Genetic mutations can increase risks for certain cancers, but this does not mean cancer will definitely develop. You should be prepared to receive positive or negative results.
      <span class="emphasis">Most people receive Negative Results meaning no mutations associated with an increased risk for the Hereditary cancers.</span>
    </p>
    <div class="web-box web-box--large">www.familyRiskCheck.com</div>
  </section>

  <section class="panel panel--cover">
    <svg class="panel-art" viewBox="0 0 560 480" role="img" aria-label="Photo of grandparents, parents and grandchildren laughing together outdoors in a park">
      <defs>
        <linearGradient id="parkTone" x1="0" y1="0" x2="1" y2="1">
          <stop offset="0" stop-color="#6f9a3f"/>
          <stop offset="0.45" stop-color="#9cc3d9"/>
          <stop offset="1" stop-color="#d8b7a6"/>
        </linearGradient>
      </defs>
      <path d="M0 30 H560 V400 Q280 440 0 452 Z" fill="url(#parkTone)"/>
      <path d="M0 452 Q280 440 560 400 V414 Q280 456 0 468 Z" fill="var(--green)"/>
    </svg>
    <div class="brand-block">
      <span class="brand-dot"></span>
      <span class="brand-name">Kinline<br>Health<br>Group</span>
    </div>

    <h1 class="cover-title">Hereditary Cancer Screening</h1>
    <p class="cover-subtitle">"The Test You Take For Them"</p>

    <div class="photo-strip">
      <div class="photo photo--a" role="img" aria-label="Grandmother and grandfather smiling with a granddaughter"></div>
      <div class="photo photo--b" role="img" aria-label="Grandfather and granddaughter posing together"></div>
      <div class="photo photo--c" role="img" aria-label="Large family group sitting together outdoors"></div>
      <div class="photo photo--d" role="img" aria-label="Granddaughter kissing her laughing grandfather"></div>
    </div>
    <div class="caption-bar">Will You give Your loved ones the information to Beat Cancer in their lives ?</div>
    <p class="cover-tagline">knowing is better than not knowing. Knowledge is Power.</p>
    <div class="web-box web-box--small">www.familyRiskCheck.com</div>
  </section>

</div>
</body>
</html>
```